Lumara Health & Wellness Business Card Design

We would like to create business cards matching with our new logo design. The card should be professional looking but still have a playful side and something that would be eye catching. We are planing to open a luxury medical spa and looking to create a design based on this new logo. We are looking for a design that shows off luxury but not be gold in color. Also, while we are a more female oriented medical center we do have men that come in for our services and it should be be too feminine.

Target Market(s)

Health & Wellness. Medical patients. Luxury spa

Industry/Entity Type

Health And Wellness

Contact Information for Business Card

It should have the logo design in the front of card and back of card should have our contact information. Our current colors are peach/ coral, teal, and gray. We are looking for a modern looking design.

Font styles to use
Script

Colors
32a6d6
e667a6
86cfc6
fece3e

Requirements
Must have
• It should have our logo design. We would prefer to have a more modern look to the card.
Nice to have
• Eye-Catching Design on the personable side but still classy.
Should not have
• At this point we are looking for the best design. It should not have color purple.

```html
<!DOCTYPE html>
<html lang="en">
<head>
<meta charset="utf-8">
<title>Lumara Health &amp; Wellness — Business Card</title>
<link rel="stylesheet" href="https://fonts.googleapis.com/css2?family=Questrial&family=Mr+Dafoe&display=swap">
<style>
  :root {
    --ink: #0b0b0b;
    --paper: #ffffff;
    --sun: #fece3e;
    --stage: #e9e6e1;
    --muted: #f2f2f2;
  }
  * { margin: 0; padding: 0; box-sizing: border-box; }
  html, body { width: 1200px; height: 880px; overflow: hidden; }
  body {
    background: var(--stage);
    position: relative;
    font-family: "Questrial", "Century Gothic", sans-serif;
  }
  .card {
    position: absolute;
    width: 560px;
    height: 320px;
    border-radius: 24px;
    overflow: hidden;
    box-shadow: 0 14px 30px rgba(0,0,0,0.22);
  }
  .card--front { left: 120px; top: 80px; background: var(--ink); }
  .card--back { left: 520px; top: 480px; background: var(--ink); }

  .brand-name {
    position: absolute;
    font-weight: 400;
    text-transform: uppercase;
    line-height: 1.2;
    text-align: center;
  }
  .card--front .brand-name {
    left: 60px; right: 60px; top: 108px;
    font-size: 40px;
    letter-spacing: 4px;
    color: var(--sun);
  }

  .back-art { position: absolute; inset: 0; }
  .card--back .brand-name {
    left: 28px; width: 240px; top: 126px;
    font-size: 24px;
    letter-spacing: 2px;
    color: var(--ink);
  }

  .contact {
    position: absolute;
    left: 368px; top: 70px;
    width: 184px;
    color: var(--muted);
  }
  .contact__name {
    font-family: "Mr Dafoe", cursive;
    font-size: 34px;
    line-height: 1;
    color: var(--paper);
  }
  .contact__role {
    font-size: 12px;
    color: var(--sun);
    margin-top: -2px;
    margin-left: 14px;
  }
  .contact__address {
    font-size: 11.5px;
    line-height: 1.45;
    margin-top: 22px;
  }
  .contact__list { list-style: none; margin-top: 14px; font-size: 11.5px; }
  .contact__item {
    display: flex;
    align-items: center;
    gap: 8px;
    line-height: 1.5;
  }
  .contact__icon { width: 11px; height: 11px; flex: none; }
</style>
</head>
<body>

  <section class="card card--front" aria-label="Card front">
    <p class="brand-name">Lumara Health &amp; Wellness</p>
  </section>

  <section class="card card--back" aria-label="Card back">
    <svg class="back-art" viewBox="0 0 560 320" width="560" height="320" aria-hidden="true">
      <path d="M240 0 C330 50 375 210 318 320 L302 320 C356 210 316 50 226 0 Z" fill="var(--sun)"/>
      <path d="M0 0 H226 C318 50 354 210 300 320 H0 Z" fill="var(--paper)"/>
    </svg>

    <p class="brand-name">Lumara Health &amp; Wellness</p>

    <div class="contact">
      <p class="contact__name">Daniel Reyes</p>
      <p class="contact__role">Owner</p>
      <p class="contact__address">PO BOX 418, Mesa Verde Road<br>Suite 6, Tucson 85704</p>
      <ul class="contact__list">
        <li class="contact__item">
          <svg class="contact__icon" viewBox="0 0 11 11" aria-hidden="true"><rect x="1" y="1" width="9" height="9" fill="none" stroke="var(--sun)" stroke-width="1.6"/></svg>
          (520) 555 0148
        </li>
        <li class="contact__item">
          <svg class="contact__icon" viewBox="0 0 11 11" aria-hidden="true"><rect x="0.5" y="2" width="10" height="7" fill="var(--sun)"/><path d="M0.5 2 L5.5 6 L10.5 2" fill="none" stroke="var(--ink)" stroke-width="0.9"/></svg>
          hello@lumarawellness.com
        </li>
        <li class="contact__item">
          <svg class="contact__icon" viewBox="0 0 11 11" aria-hidden="true"><circle cx="5.5" cy="5.5" r="5" fill="var(--sun)"/><path d="M0.5 5.5 H10.5 M5.5 0.5 C2.5 3 2.5 8 5.5 10.5 M5.5 0.5 C8.5 3 8.5 8 5.5 10.5" fill="none" stroke="var(--ink)" stroke-width="0.7"/></svg>
          www.lumarawellness.com
        </li>
      </ul>
    </div>
  </section>

</body>
</html>
```